Need Power Point Presentation - That incorporates New Logo

We have a new logo and would like to incorporate it into a Power Point template. We are looking for title page, 2 body pages and a closing page design. If you have any questions please let me know. New logo is attached.

```html
<!DOCTYPE html>
<html lang="en">
<head>
<meta charset="utf-8">
<title>KELVANT Presentation Template</title>
<link href="https://fonts.googleapis.com/css2?family=Open+Sans:wght@300;400&display=swap" rel="stylesheet">
<style>
  :root {
    --canvas: #ffffff;
    --title-light: #9cc4e4;
    --title-pale: #dcedf9;
    --brand-blue: #1b75bb;
    --brand-soft: #8ec0e6;
    --closing-blue: #0b71b9;
    --closing-name: #6cb6ea;
    --body-text: #5a5a5a;
    --white: #ffffff;
    --photo-deep: #2f6fb0;
    --photo-sky: #a9cdea;
  }
  * { margin: 0; padding: 0; box-sizing: border-box; }
  html, body { width: 1200px; height: 900px; overflow: hidden; background: var(--canvas); }
  body { position: relative; font-family: "Open Sans", "Segoe UI", sans-serif; }

  .slide { position: absolute; width: 361px; height: 278px; overflow: hidden; }
  .slide--title { left: 204px; top: 150px; background: linear-gradient(90deg, var(--title-light) 0%, #a9cbe7 50%, var(--title-pale) 100%); }
  .slide--intro { left: 635px; top: 150px; background: var(--white); }
  .slide--aviation { left: 204px; top: 456px; background: var(--white); }
  .slide--closing { left: 636px; top: 456px; width: 360px; background: var(--closing-blue); }

  .brand-name { position: absolute; font-weight: 400; letter-spacing: 0.04em; white-space: nowrap; line-height: 1; }
  .brand-name sup { font-size: 0.35em; vertical-align: top; position: relative; top: -0.2em; margin-left: 2px; }

  .slide--title .brand-name { left: 120px; top: 152px; font-size: 38px; color: var(--white); }
  .slide--intro .brand-name,
  .slide--aviation .brand-name { font-size: 17px; color: var(--brand-soft); }
  .slide--intro .brand-name { left: 246px; top: 22px; }
  .slide--aviation .brand-name { left: 246px; top: 21px; }
  .slide--closing .brand-name { left: 166px; top: 160px; font-size: 30px; color: var(--closing-name); }

  .closing-note { position: absolute; left: 227px; top: 193px; font-size: 17px; font-weight: 300; color: var(--white); }

  .slide-heading { position: absolute; font-size: 29px; font-weight: 300; color: var(--brand-blue); line-height: 1; }
  .slide-body { position: absolute; width: 290px; font-size: 13.5px; font-weight: 300; line-height: 19px; color: var(--body-text); }

  .slide--intro .slide-heading { left: 33px; top: 140px; }
  .slide--intro .slide-body { left: 33px; top: 178px; }
  .slide--aviation .slide-heading { left: 44px; top: 152px; }
  .slide--aviation .slide-body { left: 44px; top: 195px; }

  .photo-band { position: absolute; left: 0; top: 46px; width: 361px; height: 96px; display: flex; }
  .photo-band__cabin { width: 96px; height: 100%; background: linear-gradient(180deg, #7fa9d6 0%, var(--photo-deep) 100%); }
  .photo-band__sky { flex: 1; height: 100%; background: linear-gradient(160deg, #3c7fc0 0%, var(--photo-sky) 55%, #e4f0fa 100%); }
</style>
</head>
<body>

  <section class="slide slide--title">
    <div class="brand-name">KELVANT<sup>®</sup></div>
  </section>

  <section class="slide slide--intro">
    <div class="brand-name">KELVANT<sup>®</sup></div>
    <h2 class="slide-heading">Introduction</h2>
    <p class="slide-body">Lorem ipsum dolor sit amet, consectetur adipiscing elit. Aliquam sem purus, bibendum id eleifend at, tempor a arcu.</p>
  </section>

  <section class="slide slide--aviation">
    <div class="brand-name">KELVANT<sup>®</sup></div>
    <div class="photo-band">
      <div class="photo-band__cabin" role="img" aria-label="Photo of an aircraft cabin with rows of blue seats"></div>
      <div class="photo-band__sky" role="img" aria-label="Photo of a passenger jet taking off against a blue sky"></div>
    </div>
    <h2 class="slide-heading">Aviation</h2>
    <p class="slide-body">Lorem ipsum dolor sit amet, consectetur adipiscing elit. Aliquam sem purus, bibendum id eleifend at, tempor a arcu.</p>
  </section>

  <section class="slide slide--closing">
    <div class="brand-name">KELVANT<sup>®</sup></div>
    <p class="closing-note">Thank You</p>
  </section>

</body>
</html>
```